Harlow Pennick Group Business Cards

We have a new logo, and want to design new business cards with it. We are 21 years in business, and want a fresh but professional look, so not a lot of extra stuff on the card. We are a recruiting and staffing firm focused on placing accounting and finance professionals in the Dallas TX area. I've attached our new logo that should be displayed on the cards. Here is what I think we want on the cards:
Ned Varcombe, CPA
Partner and Managing Director
8262 Quarry Mill Rd.
Suite 610
Dallas, TX 75391
O 214-583-9071
M 214-690-1482
ned@harlowpennick-example.com
www.harlowpennick-example.com

```html
<!DOCTYPE html>
<html lang="en">
<head>
<meta charset="utf-8">
<title>Harlow Pennick Group Business Cards</title>
<link href="https://fonts.googleapis.com/css2?family=Lato:wght@400;700;900&family=Josefin+Sans:wght@700&display=swap" rel="stylesheet">
<style>
  :root {
    --backdrop: #e6e6e6;
    --card-white: #ececec;
    --navy: #0033a0;
    --mid-blue: #5273bc;
    --ink: #1a1a1a;
    --white: #ffffff;
  }
  html, body {
    margin: 0;
    width: 1200px;
    height: 1200px;
    overflow: hidden;
    background: var(--backdrop);
  }
  .canvas {
    position: relative;
    width: 1200px;
    height: 1200px;
  }
  .card {
    position: absolute;
    top: 310px;
    height: 594px;
    box-shadow: 0 2px 6px rgba(0,0,0,0.25);
    overflow: hidden;
  }
  .card-front {
    left: 234px;
    width: 364px;
    background: var(--card-white);
    font-family: "Lato", sans-serif;
    text-align: center;
    color: var(--ink);
  }
  .brand-name {
    position: absolute;
    top: 430px;
    left: 0;
    right: 0;
    top: 118px;
    font-family: "Lato", sans-serif;
    font-weight: 900;
    color: var(--navy);
    font-size: 29px;
    line-height: 36px;
    letter-spacing: 0.5px;
    text-transform: uppercase;
  }
  .brand-mark {
    display: block;
    width: 14px;
    height: 14px;
    margin: 0 auto 12px;
    background: var(--navy);
  }
  .contact-block {
    position: absolute;
    left: 0;
    right: 0;
    top: 343px;
  }
  .person-name {
    font-family: "Josefin Sans", sans-serif;
    font-weight: 700;
    font-size: 23px;
    color: var(--navy);
    margin: 0;
    line-height: 28px;
  }
  .person-name .credential {
    color: var(--mid-blue);
    font-size: 19px;
  }
  .person-title {
    font-size: 16px;
    margin: 0;
    line-height: 20px;
  }
  .rule {
    width: 190px;
    height: 1px;
    background: var(--mid-blue);
    margin: 10px auto 7px;
  }
  .contact-lines {
    font-size: 16.5px;
    line-height: 22px;
    margin: 0;
  }
  .contact-lines .label { color: var(--navy); }
  .contact-lines .web { color: var(--navy); }
  .contact-lines .web span { color: var(--mid-blue); }
  .address {
    font-size: 16.5px;
    line-height: 21px;
    margin: 0;
  }

  .card-back {
    left: 627px;
    width: 370px;
    background: var(--navy);
    font-family: "Lato", sans-serif;
  }
  .card-back svg.split {
    position: absolute;
    inset: 0;
  }
  .back-name {
    position: absolute;
    left: 0;
    right: 0;
    top: 228px;
    text-align: center;
    font-weight: 900;
    color: var(--white);
    font-size: 44px;
    line-height: 52px;
    text-transform: uppercase;
  }
  .back-web {
    position: absolute;
    left: 0;
    right: 0;
    top: 523px;
    text-align: center;
    color: var(--white);
    font-size: 16.5px;
    font-weight: 700;
  }
</style>
</head>
<body>
<main class="canvas">
  <section class="card card-front" aria-label="Business card front">
    <div class="brand-name"><span class="brand-mark"></span>Harlow Pennick<br>Group</div>
    <div class="contact-block">
      <p class="person-name">NED VARCOMBE, <span class="credential">CPA</span></p>
      <p class="person-title">Partner and Managing Director</p>
      <div class="rule"></div>
      <p class="contact-lines">
        <span class="label">P:</span> 214-583-9071<br>
        <span class="label">M:</span> 214-690-1482<br>
        <span class="label">E:</span> ned@harlowpennick-example.com<br>
        <span class="web">www.<span>harlowpennick-example</span>.com</span>
      </p>
      <div class="rule"></div>
      <p class="address">8262 Quarry Mill Rd.<br>Suite 610 Dallas, TX 75391</p>
    </div>
  </section>

  <section class="card card-back" aria-label="Business card back">
    <svg class="split" width="370" height="594" viewBox="0 0 370 594" aria-hidden="true">
      <polygon points="0,0 370,0 370,458 0,66" fill="var(--mid-blue)"/>
    </svg>
    <div class="back-name">Harlow<br>Pennick</div>
    <div class="back-web">www.harlowpennick-example.com</div>
  </section>
</main>
</body>
</html>
```